job report

Designer – Professional Plumbing Job Report Template

Overview

We are seeking a skilled designer to create a professional, easy-to-use Job Report template for a commercial and maintenance plumbing business.
The report will be used for clients, property managers, facilities managers, strata, and retail centres and must clearly communicate findings, works completed, and recommendations in a polished, compliant, and branded format.

The final document must be suitable for PDF delivery, email, and ongoing reuse.

Objectives

Present plumbing works in a clear, professional, and defensible report format

Improve client understanding of findings and recommendations

Provide a repeatable template that can be used across maintenance, reactive, and investigative works

Allow easy insertion of text, tables, and photos

Report Structure (Minimum Inclusions)
1. Cover Page

Company logo and branding

Report title (e.g. Plumbing Job Report / Investigation Report)

Client name

Site address

Job reference / work order number

Date of attendance

Technician / contractor name

2. Client & Site Details

Client / company name

Site address

Contact person

Contact details

Access notes (after-hours, tenant access, etc.)

3. Reason for Attendance

Clear description of why attendance was required

Call-out type (reactive, scheduled maintenance, investigation, emergency, etc.)

Reported issue or scope requested by client

4. Findings / Observations

Detailed findings discovered on site

Condition of pipework, fixtures, drainage, or systems

Any contributing factors identified

Notes on compliance, wear, damage, or risk

(This section should support bullet points and paragraphs.)

5. Works Carried Out

Step-by-step description of works completed

Equipment used (e.g. jetter, CCTV camera, leak detection, flex shaft, etc.)

Repairs, replacements, testing, and verification

Confirmation that systems were tested and operational on completion

6. Photos & Visual Evidence

Clearly labelled photo sections

Before / during / after photos

Space for photo captions and explanations

Logical layout that aligns photos with written findings

7. Recommendations

Clearly separated from works completed

Urgent vs non-urgent recommendations

Preventative maintenance advice

Upgrade or replacement suggestions

Risk-based language where appropriate

8. Limitations & Exclusions

Areas not inspected

Access limitations

Assumptions made during inspection

Items outside scope of works

9. Conclusion

Summary of outcome

Confirmation of current system status

Next steps (if any)

10. Sign-Off

Contractor / technician name

Company name

Date

Optional client acknowledgement section

Design Requirements

Clean, professional layout

Commercial / trade-appropriate styling (not overly creative)

Easy-to-read fonts

Consistent headings and spacing

Logical flow for busy property managers

Editable format (Word / Google Docs / InDesign source file)

Final export-ready PDF version

Bonus (Nice to Have)

Traffic-light system (Green / Amber / Red) for condition reporting

Iconography for findings, repairs, and recommendations

Optional sections for compliance notes (AS/NCC references)

Space for QR codes or job reference numbers

Deliverables

Editable master report template

PDF version

Instructions or notes for ongoing use

```html
<!DOCTYPE html>
<html lang="en">
<head>
<meta charset="utf-8">
<title>Plumbing Job Report – Template Pages</title>
<link href="https://fonts.googleapis.com/css2?family=Poppins:wght@400;500;600;700;800&display=swap" rel="stylesheet">
<style>
:root{
  --blue:#1ea7df;
  --blue-soft:#9fd8ef;
  --yellow:#f5b31a;
  --cream:#fde6b0;
  --sky:#d9f0fa;
  --ink:#2b2b2b;
  --text:#555;
  --band:#ececec;
  --stage:#b4b4b4;
}
*{box-sizing:border-box;margin:0;padding:0}
html,body{width:1200px;height:3541px;overflow:hidden}
body{background:var(--stage);position:relative;font-family:'Poppins',sans-serif;color:var(--ink)}
.page{position:absolute;width:489px;height:633px;background:#fff;overflow:hidden}
.col-l{left:89px}.col-r{left:623px}
.row1{top:78px}.row2{top:767px}.row3{top:1456px}.row4{top:2135px}.row5{top:2815px;height:646px}
.abs{position:absolute}
.page-head{position:absolute;left:26px;right:26px;top:24px;height:14px;border-bottom:1px solid var(--blue-soft);display:flex;align-items:center;gap:5px;padding-bottom:10px}
.page-head .dot{width:9px;height:9px;border-radius:50%;background:var(--yellow)}
.page-head span{font-size:7.5px;font-weight:500;color:var(--blue);letter-spacing:.2px}
.page-title{position:absolute;left:26px;top:62px;font-size:22px;font-weight:500;color:var(--ink)}
.page-foot{position:absolute;left:26px;right:26px;bottom:20px;border-bottom:1px solid var(--blue-soft);display:flex;justify-content:space-between;align-items:flex-end;padding-bottom:3px}
.brand-mini{font-size:8px;font-weight:700;color:var(--blue);line-height:1}
.page-no{font-size:6px;background:var(--blue);color:#fff;padding:1px 3px}
p,.txt{font-size:7px;line-height:1.5;color:var(--text);text-align:justify}
h3{font-size:13px;font-weight:500;color:var(--ink)}
h4{font-size:11.5px;font-weight:500;color:var(--ink)}
.photo{background:linear-gradient(135deg,#7d8c99,#c9ced3)}
.photo.dark{background:linear-gradient(135deg,#1e3a44,#4f7785)}
.photo.warm{background:linear-gradient(135deg,#d8cfc3,#9b8f80)}
.brand{font-weight:700;color:var(--blue);line-height:1;text-align:center}
.cover-title{position:absolute;left:73px;top:362px;font-size:56px;font-weight:800;color:var(--blue);letter-spacing:1px;line-height:1}
.cover-band{position:absolute;left:73px;top:420px;width:346px;height:34px;border-bottom:2px solid var(--yellow)}
.cover-band span{display:inline-block;background:var(--yellow);color:#fff;font-size:25px;font-weight:800;padding:0 10px;line-height:34px;letter-spacing:1px}
.cover-fields{position:absolute;left:73px;top:474px;width:346px;display:flex;justify-content:space-between;text-align:center}
.label{font-size:9px;font-weight:600;color:var(--blue)}
.value{font-size:8px;color:var(--ink)}
.cover-band-grey{position:absolute;left:0;right:0;top:545px;height:68px;background:var(--band);display:flex;justify-content:space-between;padding:16px 73px 0}
.cover-band-grey .label{font-weight:500;font-size:8px}
.card{position:absolute;background:var(--cream)}
.check{display:inline-block;width:6px;height:6px;border:1px solid #999;vertical-align:-1px;margin:0 2px 0 4px}
.kv{font-size:6.5px;color:var(--text);line-height:1.7;text-align:right}
.kv b{color:var(--ink);font-weight:600}
.bullet{font-size:7px;line-height:1.45;color:var(--text);padding-left:9px;position:relative;margin-bottom:9px}
.bullet::before{content:"";position:absolute;left:0;top:3px;width:4px;height:4px;border-radius:50%;background:var(--blue)}
.call-item{position:absolute;left:0;right:0;display:flex;gap:10px}
.call-icon{width:40px;height:40px;border-radius:50%;background:#fff;border:2px solid var(--blue-soft);display:flex;align-items:center;justify-content:center;flex:none}
.finding h4{margin-bottom:6px}
.finding .bullet{margin-bottom:6px}
.step{position:absolute;width:110px;font-size:7px;color:var(--text);line-height:1.45}
.step b{display:block;color:var(--ink);font-weight:600;font-size:7.5px}
.equip{font-size:8px;color:var(--ink);line-height:2.15}
.equip b{font-weight:600}
.gal-row{position:absolute;left:26px;right:26px;height:124px;display:flex}
.gal-row .photo{width:150px;flex:none}
.gal-row .panel{flex:1;padding:12px 20px}
.gal-row h4{font-size:12px;margin-bottom:5px}
.rec-col{position:absolute;width:134px;text-align:center}
.vs-panel{position:absolute;top:289px;height:151px}
.vs-head{height:22px;font-size:10px;text-align:center;line-height:22px;border:1px solid var(--blue-soft)}
.vs-panel p{margin:12px 12px 0;text-align:left}
</style>
</head>
<body>

<!-- PAGE 1 : COVER -->
<section class="page col-l row1">
  <div class="abs brand" style="left:300px;top:40px;width:150px;font-size:20px">TIDEWELL<br>PLUMBING</div>
  <svg class="abs" style="left:120px;top:50px" width="240" height="305" viewBox="0 0 240 305" role="img" aria-label="Photo of a plumber working under a sink, framed in a water-drop shape">
    <defs><linearGradient id="dropfill" x1="0" y1="0" x2="1" y2="1"><stop offset="0" stop-color="#dfe5ea"/><stop offset="1" stop-color="#7e8ea0"/></linearGradient></defs>
    <path d="M120 8 C150 70 225 130 225 195 A105 105 0 0 1 15 195 C15 130 90 70 120 8Z" fill="url(#dropfill)" stroke="#1ea7df" stroke-width="2"/>
  </svg>
  <div class="cover-title">PLUMBING</div>
  <div class="cover-band"><span>JOB REPORT</span></div>
  <div class="cover-fields">
    <div><div class="label">CLIENT NAME</div><div class="value">Name Here</div></div>
    <div><div class="label">SITE ADDRESS</div><div class="value">Address Here</div></div>
    <div><div class="label">JOB REFERENCE</div><div class="value">Address Here</div></div>
  </div>
  <div class="cover-band-grey">
    <div><div class="label">Date of Attendance :</div><div class="value" style="font-size:7px;margin-top:6px">00/00/0000</div></div>
    <div style="text-align:right"><div class="label">Technician / Contractor Name :</div><div class="value" style="font-size:7px;margin-top:6px">Name Here</div></div>
  </div>
</section>

<!-- PAGE 2 : CLIENT & SITE -->
<section class="page col-r row1">
  <div class="page-head"><i class="dot"></i><span>PLUMBING JOB REPORT</span></div>
  <h2 class="page-title">Client &amp; Site Details</h2>
  <div class="card" style="left:26px;top:105px;width:437px;height:175px">
    <div class="abs photo warm" style="left:14px;top:18px;width:118px;height:140px" role="img" aria-label="Portrait photo of the client contact"></div>
    <div class="abs" style="left:148px;top:18px;width:272px">
      <h3 style="font-size:13px">Client Name Here</h3>
      <div style="font-size:7.5px;color:var(--ink);margin:3px 0 6px">
        <svg width="8" height="8" viewBox="0 0 10 10"><path d="M5 1a3 3 0 0 1 3 3c0 2-3 5-3 5S2 6 2 4a3 3 0 0 1 3-3z" fill="#333"/></svg> (Client Address Here)
        <svg width="8" height="8" viewBox="0 0 10 10" style="margin-left:4px"><circle cx="5" cy="5" r="5" fill="#333"/><path d="M3 3l1.2-.4.8 1.6-.7.6a3 3 0 0 0 1 1l.6-.7 1.6.8L7 7C5 7 3 5 3 3z" fill="#fff"/></svg> (0400–555–218)
      </div>
      <p>This panel holds the client overview. Add the company name, the main contact person, preferred phone and email, and any notes about how the client wishes to receive reports. Keep it short so a property manager can confirm the details at a glance before reading the findings and recommendations.</p>
    </div>
  </div>
  <div class="abs" style="left:26px;top:290px;width:266px;text-align:right">
    <h3 style="font-size:13px">Site Name Here</h3>
    <div style="font-size:7.5px;color:var(--ink);margin:2px 0 12px">
      <svg width="8" height="8" viewBox="0 0 10 10"><path d="M5 1a3 3 0 0 1 3 3c0 2-3 5-3 5S2 6 2 4a3 3 0 0 1 3-3z" fill="#333"/></svg> (Site Address Here)</div>
    <div class="kv"><b>Property Type:</b><i class="check"></i>Residential<i class="check"></i>Commercial<i class="check"></i>Industrial</div>
    <div class="kv"><b>Building Type:</b><i class="check"></i>House<i class="check"></i>Apartment<i class="check"></i>Office<i class="check"></i>Retail<i class="check"></i>Other</div>
    <div class="kv" style="margin-top:4px"><b>Type of Service Required:</b><i class="check"></i>Installation<i class="check"></i>Repair<br><i class="check"></i>Maintenance<i class="check"></i>Inspection Emergency</div>
    <div class="kv" style="margin-top:4px"><b style="font-size:7.5px">Access notes</b></div>
    <div class="kv"><b>Parking Available:</b><i class="check"></i>Yes<i class="check"></i>No</div>
    <div class="kv"><b>Pets on Site:</b><i class="check"></i>Yes<i class="check"></i>No</div>
    <div class="kv"><b>Special Safety Requirements:</b></div>
  </div>
  <div class="abs photo" style="left:301px;top:290px;width:162px;height:161px" role="img" aria-label="Photo of a technician recording notes on a tablet beside pipework"></div>
  <div class="abs photo dark" style="left:26px;top:469px;width:141px;height:93px" role="img" aria-label="Photo of a wrench tightening a pipe fitting"></div>
  <div class="abs photo warm" style="left:174px;top:469px;width:141px;height:93px" role="img" aria-label="Photo of gloved hands repairing a pipe"></div>
  <div class="abs photo" style="left:322px;top:469px;width:141px;height:93px" role="img" aria-label="Photo of chrome pipework and valves"></div>
  <div class="page-foot"><span class="brand-mini">TIDEWELL</span><span class="page-no">02</span></div>
</section>

<!-- PAGE 3 : REASON FOR ATTENDANCE -->
<section class="page col-l row2">
  <div class="page-head"><i class="dot"></i><span>PLUMBING JOB REPORT</span></div>
  <h2 class="page-title">Reason for Attendance</h2>
  <p class="abs" style="left:26px;right:26px;top:100px">Describe clearly why attendance was required on site. Note who raised the request, the date it was logged, the symptoms reported and any earlier visits. This summary gives property and facilities managers a quick view of the problem before they read the detailed findings, works and recommendations in the sections that follow.</p>
  <h3 class="abs" style="left:26px;top:184px">Reported Issue:</h3>
  <div class="abs" style="left:26px;top:206px;width:160px">
    <div class="bullet">Issue reported by the client, with location on site and time first noticed.</div>
    <div class="bullet">Symptoms described, such as leaks, low pressure, blockage or odour.</div>
    <div class="bullet">Any earlier repairs or attendances noted by the site contact.</div>
    <div class="bullet">Risk to tenants, stock or services raised at time of booking.</div>
  </div>
  <h3 class="abs" style="left:26px;top:374px;line-height:1.2">Scope of Work<br>Requested:</h3>
  <div class="abs txt" style="left:26px;top:412px;width:160px;color:var(--ink)">Inspection &nbsp;|&nbsp; Repair &nbsp;|&nbsp; Maintenance &nbsp;|&nbsp; Installation</div>
  <div class="abs photo" style="left:26px;top:467px;width:158px;height:83px" role="img" aria-label="Photo of a plumber kneeling beside a kitchen cabinet"></div>
  <div class="card" style="left:230px;top:188px;width:233px;height:362px"></div>
  <div class="abs" style="left:206px;top:202px;width:250px;height:340px">
    <div class="call-item" style="top:10px"><div class="call-icon"><svg width="20" height="20" viewBox="0 0 20 20" fill="none" stroke="#1ea7df" stroke-width="1.5"><circle cx="10" cy="10" r="7"/><path d="M10 6v4l3 2"/></svg></div><div><h4>Reactive</h4><p style="margin-top:2px">Unplanned call-out raised after a fault or failure was reported on site.</p></div></div>
    <div class="call-item" style="top:95px"><div class="call-icon"><svg width="20" height="20" viewBox="0 0 20 20" fill="none" stroke="#1ea7df" stroke-width="1.5"><circle cx="10" cy="10" r="7"/><circle cx="10" cy="10" r="3"/></svg></div><div><h4>Scheduled Maintenance</h4><p style="margin-top:2px">Planned service visit carried out under the agreed maintenance program.</p></div></div>
    <div class="call-item" style="top:182px"><div class="call-icon"><svg width="20" height="20" viewBox="0 0 20 20" fill="none" stroke="#1ea7df" stroke-width="1.5"><circle cx="9" cy="9" r="5"/><path d="M13 13l4 4"/></svg></div><div><h4>Investigation</h4><p style="margin-top:2px">Attendance to locate the cause of a fault and report on options.</p></div></div>
    <div class="call-item" style="top:268px"><div class="call-icon"><svg width="20" height="20" viewBox="0 0 20 20" fill="none" stroke="#1ea7df" stroke-width="1.5"><path d="M10 3l7 13H3z"/><path d="M10 8v4M10 14v.5"/></svg></div><div><h4>Emergency</h4><p style="margin-top:2px">Urgent response to make safe, stop water loss or restore service.</p></div></div>
  </div>
  <div class="page-foot"><span class="brand-mini">TIDEWELL</span><span class="page-no">03</span></div>
</section>

<!-- PAGE 4 : FINDINGS -->
<section class="page col-r row2">
  <div class="page-head"><i class="dot"></i><span>PLUMBING JOB REPORT</span></div>
  <h2 class="page-title">Findings / Observations</h2>
  <div class="card" style="left:26px;top:104px;width:437px;height:468px"></div>
  <div class="abs" style="left:45px;top:104px;width:66px;height:468px;background:#fff"></div>
  <svg class="abs" style="left:45px;top:104px" width="66" height="468" viewBox="0 0 66 468">
    <line x1="31" y1="10" x2="31" y2="458" stroke="#1ea7df" stroke-width="1"/>
    <g fill="#1ea7df"><circle cx="31" cy="24" r="3.5"/><circle cx="31" cy="135" r="3.5"/><circle cx="31" cy="246" r="3.5"/><circle cx="31" cy="361" r="3.5"/></g>
    <g stroke="#1ea7df" stroke-width=".6"><line x1="31" y1="24" x2="66" y2="24"/><line x1="31" y1="135" x2="66" y2="135"/><line x1="31" y1="246" x2="66" y2="246"/><line x1="31" y1="361" x2="66" y2="361"/></g>
  </svg>
  <div class="abs" style="left:124px;top:118px;width:325px">
    <div class="finding" style="height:111px"><h4>System Condition</h4>
      <div class="bullet">General condition of pipework, fixtures, drainage and hot water units as found on arrival, including age and material.</div>
      <div class="bullet">Visible wear, corrosion, movement or staining noted during the inspection of each area.</div></div>
    <div class="finding" style="height:111px"><h4>Identified Issues</h4>
      <div class="bullet">Faults found on site with location, severity and any photo reference for easy cross checking.</div>
      <div class="bullet">Damage or risks to the building, occupants or services that need attention now or later.</div></div>
    <div class="finding" style="height:115px"><h4>Contributing Factors</h4>
      <div class="bullet">Causes that led to the fault, such as root intrusion, blockage, poor falls or past repairs.</div>
      <div class="bullet">Site conditions, usage patterns or tenant activity likely to affect the system over time.</div></div>
    <div class="finding"><h4>Compliance &amp; Safety</h4>
      <div class="bullet">Notes on compliance with current standards and codes, with clause references where relevant.</div>
      <div class="bullet">Safety hazards identified and any make-safe actions taken before leaving the site.</div></div>
  </div>
  <div class="page-foot"><span class="brand-mini">TIDEWELL</span><span class="page-no">04</span></div>
</section>

<!-- PAGE 5 : WORKS CARRIED OUT -->
<section class="page col-l row3">
  <div class="page-head"><i class="dot"></i><span>PLUMBING JOB REPORT</span></div>
  <h2 class="page-title">Works Carried Out</h2>
  <div class="abs" style="left:26px;top:100px;font-size:11.5px;color:var(--ink)">Step-By-Step Description of Works Completed</div>
  <svg class="abs" style="left:26px;top:190px" width="437" height="110" viewBox="0 0 437 110">
    <path d="M21 16 H400 a22 22 0 0 1 22 22 v34 a22 22 0 0 1 -22 22 H162" fill="none" stroke="#1ea7df" stroke-width="1"/>
    <g fill="#fff" stroke="#1ea7df" stroke-width="1"><circle cx="21" cy="16" r="10"/><circle cx="162" cy="16" r="10"/><circle cx="298" cy="16" r="10"/><circle cx="298" cy="94" r="10"/><circle cx="162" cy="94" r="10"/></g>
    <g font-family="Poppins, sans-serif" font-size="7" fill="#1ea7df" text-anchor="middle"><text x="21" y="18.5">01</text><text x="162" y="18.5">02</text><text x="298" y="18.5">03</text><text x="298" y="96.5">04</text><text x="162" y="96.5">05</text></g>
  </svg>
  <div class="step" style="left:66px;top:141px"><b>Step 1</b>Isolate water supply and make the work area safe.</div>
  <div class="step" style="left:208px;top:141px"><b>Step 2</b>Inspect the system and confirm the fault location.</div>
  <div class="step" style="left:344px;top:141px"><b>Step 3</b>Carry out the repair and replace failed parts.</div>
  <div class="step" style="left:208px;top:220px"><b>Step 5</b>Restore supply and clean the work area on exit.</div>
  <div class="step" style="left:344px;top:220px"><b>Step 4</b>Test the system under pressure and check for leaks.</div>
  <h3 class="abs" style="left:26px;top:316px">Equipment Used</h3>
  <div class="abs equip" style="left:26px;top:336px;width:437px">
    <div><b>High-Pressure Jetter :</b> Used to clear blockages and scour the main drain line.</div>
    <div><b>CCTV Drain Camera :</b> Used to inspect pipe condition and record the footage.</div>
    <div><b>Leak Detection Equipment :</b> Used to trace the hidden leak location.</div>
    <div><b>Flex Shaft System :</b> Used to remove roots and scale from the pipe walls.</div>
    <div><b>Pipe Locators :</b> Used to trace and mark the pipe route and depth.</div>
    <div><b>Pressure Testing Tools :</b> Used to confirm the system holds pressure.</div>
  </div>
  <h3 class="abs" style="left:26px;top:467px">Repairs &amp; Replacements</h3>
  <p class="abs" style="left:26px;top:486px;width:210px">List each repair or replacement made, with the part, size and material used. Note the location on site and any photo references so the client can match the work to the findings and invoice.</p>
  <h3 class="abs" style="left:253px;top:467px">Testing &amp; Verification</h3>
  <p class="abs" style="left:253px;top:486px;width:210px">Record the tests carried out after the works, the results and readings taken. Confirm all systems were tested and found operational on completion, and note any item that still needs follow-up.</p>
  <div class="page-foot"><span class="brand-mini">TIDEWELL</span><span class="page-no">05</span></div>
</section>

<!-- PAGE 6 : GALLERY -->
<section class="page col-r row3">
  <div class="page-head"><i class="dot"></i><span>PLUMBING JOB REPORT</span></div>
  <h2 class="page-title">Our Work Gallery</h2>
  <p class="abs" style="left:26px;right:26px;top:100px">Photos below show the condition of the system before, during and after the works. Each image is labelled and paired with a short caption so the visual evidence lines up with the written findings and the works carried out sections of this report.</p>
  <div class="gal-row" style="top:166px">
    <div class="photo" role="img" aria-label="Before photo of a worn floor drain grate"></div>
    <div class="panel" style="background:var(--cream)"><h4>Before Work</h4><p>Condition of the fixture on arrival, showing build-up, staining and wear around the drain grate. Note the location, the reported issue and the reference number used in the findings section so the reader can cross check each image.</p></div>
  </div>
  <div class="gal-row" style="top:305px">
    <div class="photo" style="background:linear-gradient(135deg,#2a4fb0,#9fb4c9)" role="img" aria-label="During photo of a gloved hand cleaning the drain grate"></div>
    <div class="panel" style="background:var(--sky)"><h4>During Work</h4><p>Works in progress, showing the cleaning and repair method used on the drain. Describe the tools and steps shown, and any issues found once the fixture was opened up or the access panel was removed.</p></div>
  </div>
  <div class="gal-row" style="top:443px">
    <div class="photo" role="img" aria-label="After photo of the clean restored drain grate"></div>
    <div class="panel" style="background:var(--cream)"><h4>After Work</h4><p>Completed result after testing, showing the fixture clean, sealed and working. Confirm the outcome in a sentence and note any follow-up items listed in the recommendations section of this report.</p></div>
  </div>
  <div class="page-foot"><span class="brand-mini">TIDEWELL</span><span class="page-no">06</span></div>
</section>

<!-- PAGE 7 : RECOMMENDATIONS -->
<section class="page col-l row4">
  <div class="page-head"><i class="dot"></i><span>PLUMBING JOB REPORT</span></div>
  <h2 class="page-title">Recommendations</h2>
  <h4 class="abs" style="left:26px;top:98px;font-size:12px">Works Completed</h4>
  <div class="rec-col" style="left:26px;top:124px"><svg width="14" height="14" viewBox="0 0 14 14" fill="none" stroke="#f5b31a" stroke-width="1.3"><circle cx="7" cy="7" r="5.5"/><path d="M4.5 7l2 2 3.5-4"/></svg><p style="text-align:justify;margin-top:4px">Summary of the works finished on this visit, kept apart from the advice below so the client can see what is already done.</p></div>
  <div class="rec-col" style="left:178px;top:124px"><svg width="14" height="14" viewBox="0 0 14 14" fill="none" stroke="#f5b31a" stroke-width="1.3"><circle cx="7" cy="7" r="5.5"/><path d="M4.5 7l2 2 3.5-4"/></svg><p style="text-align:justify;margin-top:4px">Preventative maintenance advice to reduce repeat faults, such as routine jetting, flushing or checks on valves and seals.</p></div>
  <div class="rec-col" style="left:329px;top:124px"><svg width="14" height="14" viewBox="0 0 14 14" fill="none" stroke="#1ea7df" stroke-width="1.3"><circle cx="7" cy="7" r="5.5"/><path d="M4.5 7l2 2 3.5-4"/></svg><p style="text-align:justify;margin-top:4px">Timing guidance for each item so the client can plan budgets and book the next service visit in advance.</p></div>
  <h4 class="abs" style="left:26px;top:261px;font-size:12px">Urgent vs Non-urgent Recommendations</h4>
  <div class="vs-panel" style="left:26px;width:206px;background:var(--cream)">
    <div class="vs-head" style="border-color:var(--cream);background:var(--cream)">Urgent</div>
    <p>Action needed now to prevent damage or a safety risk on site.</p>
    <p>Replace failed fitting before further water loss occurs.</p>
    <p>Repair cracked section of drain within seven days.</p>
  </div>
  <div class="vs-panel" style="left:240px;width:223px;background:#fff">
    <div class="vs-head" style="background:var(--sky)">Non - Urgent</div>
    <p>Items to plan for within the next service cycle or budget.</p>
    <p>Upgrade ageing tapware to reduce future leak risk.</p>
    <p>Schedule camera inspection of main line in twelve months.</p>
  </div>
  <svg class="abs" style="left:220px;top:280px" width="32" height="32" viewBox="0 0 32 32"><circle cx="16" cy="16" r="15" fill="#fff"/><text x="16" y="21" text-anchor="middle" font-family="Poppins, sans-serif" font-weight="800" font-style="italic" font-size="13" fill="#2b2b2b">VS</text></svg>
  <h4 class="abs" style="left:26px;top:462px;font-size:11px;line-height:1.35">Upgrade or<br>Replacement<br>Suggestions</h4>
  <p class="abs" style="left:128px;top:462px;width:335px">Suggest upgrades or replacements where parts are near the end of service life. Explain the benefit to the client, the expected lifespan and a rough priority so decisions can be made with confidence.</p>
  <p class="abs" style="left:26px;top:538px;width:320px">Describe the likely outcome if advice is not followed, using clear risk-based wording such as likely, possible or unlikely, so the client understands the urgency.</p>
  <h4 class="abs" style="left:346px;top:536px;font-size:11px;line-height:1.35;text-align:right;width:117px">Risk-based<br>language</h4>
  <div class="page-foot"><span class="brand-mini">TIDEWELL</span><span class="page-no">07</span></div>
</section>

<!-- PAGE 8 : LIMITATIONS -->
<section class="page col-r row4">
  <div class="page-head"><i class="dot"></i><span>PLUMBING JOB REPORT</span></div>
  <h2 class="page-title">Limitations &amp; Exclusions</h2>
  <h4 class="abs" style="left:26px;top:112px;font-size:11px;line-height:1.3">Areas Not<br>Inspected</h4>
  <div class="abs" style="left:96px;top:108px;width:367px;height:48px;background:#f1f1f1;padding:6px 8px"><p>List any areas that were not inspected during this visit, such as locked rooms, ceiling spaces or buried pipework, and explain the reason each area was excluded.</p></div>
  <h4 class="abs" style="left:26px;top:170px;font-size:11px">Access Limitations</h4>
  <div class="abs" style="left:26px;top:190px;width:208px">
    <div class="bullet">Parts of the system were hidden behind fixed walls, floors or joinery and could not be viewed.</div>
    <div class="bullet">Tenant areas were not available at the time of attendance and need a return visit.</div>
    <div class="bullet">Roof or height access needs equipment not on site during this attendance.</div>
  </div>
  <div class="abs photo" style="left:249px;top:176px;width:214px;height:326px" role="img" aria-label="Photo of a technician writing on a clipboard on site"></div>
  <h4 class="abs" style="left:26px;top:372px;font-size:11px;line-height:1.3">Assumptions made<br>during inspection</h4>
  <p class="abs" style="left:26px;top:404px;width:208px">State any assumptions made, for example that hidden pipework matches the visible sections, or that plans supplied by the client are accurate and current.</p>
  <h4 class="abs" style="left:26px;top:512px;font-size:11px">Items Outside Scope of Works</h4>
  <p class="abs" style="left:26px;right:26px;top:530px">Note any items outside the scope of this job, such as electrical, building or gas works, which should be referred to the relevant trade for advice.</p>
  <div class="page-foot"><span class="brand-mini">TIDEWELL</span><span class="page-no">08</span></div>
</section>

<!-- PAGE 9 : CONCLUSION -->
<section class="page col-l row5">
  <div class="page-head"><i class="dot"></i><span>PLUMBING JOB REPORT</span></div>
  <h2 class="page-title">Conclusion</h2>
  <h4 class="abs" style="left:26px;top:98px;font-size:12px">Summary of Outcome</h4>
  <div class="abs" style="left:26px;right:26px;top:122px">
    <p>This section summarises the outcome of the attendance in plain terms. Restate why the visit was needed, what was found on site and what was done to resolve the issue. Confirm the current status of each system inspected, noting whether it is fully operational, operating with limits, or isolated pending further works. Where parts or access were not available, explain the temporary measures put in place and how long they are expected to last. Keep the wording clear and factual so a busy property manager can read the summary alone and understand the position without reading the full report. Refer back to the photo references and finding numbers where helpful, so each statement can be checked against the evidence provided in earlier sections. If any risk remains on site, state it plainly and point the reader to the urgent recommendations. Note who was present on site, who was advised of the outcome, and whether the client or tenant accepted the works at the time of completion.</p>
    <p style="margin-top:8px">Set out the next steps, if any, such as a quote for recommended works, a return visit to complete deferred items, or a scheduled maintenance date. Include the contact details for follow-up questions and the job reference to quote when booking. Close with the technician name, company name and date of sign-off, and leave space for an optional client acknowledgement if required by the site or contract. This confirms the report is complete and ready to be filed with the maintenance records for the property.</p>
  </div>
  <div class="page-foot"><span class="brand-mini">TIDEWELL</span><span class="page-no">09</span></div>
</section>

<!-- PAGE 10 : BACK COVER -->
<section class="page col-r row5" style="background:#f3f3f3">
  <div class="abs" style="left:0;right:0;top:506px;bottom:0;background:#fff"></div>
  <div class="abs brand" style="left:0;right:0;top:44px;font-size:22px">TIDEWELL<br>PLUMBING</div>
  <div class="abs photo dark" style="left:69px;top:162px;width:335px;height:211px" role="img" aria-label="Photo of hands using a red wrench on a chrome pipe"></div>
  <p class="abs" style="left:100px;width:289px;top:390px;text-align:center;font-size:8px;color:var(--ink)">Thank you for choosing our team. For questions about this report, please quote the job reference when you contact us.</p>
  <div class="abs" style="left:0;right:0;top:440px;text-align:center;font-size:18px;font-weight:700;color:var(--blue)">TIDEWELL PLUMBING</div>
  <div class="abs" style="left:73px;right:73px;top:566px;display:flex;justify-content:space-between">
    <div><div class="label" style="font-weight:500;font-size:8px">Date of Attendance :</div><div class="value" style="font-size:7px;margin-top:4px">00/00/0000</div></div>
    <div style="text-align:right"><div class="label" style="font-weight:500;font-size:8px">Technician / Contractor Name :</div><div class="value" style="font-size:7px;margin-top:4px">Name Here</div></div>
  </div>
</section>

</body>
</html>
```